Cobalt Reclaim Partners is a recycling company. We have started a marketing campaign and would love your artwork to help us get started. We would like the fallowing to be on our postcard:
At the top please write: Now servicing businesses in the city of Industry!
Below that we would like 3 pictures.. The first is a picture of trash, the second is a our logo and at plus sign. After that would be a picture of neat baled recycled material and the last picture would be money. Below this please right the following:
- Companies choose cobalt reclaim partners because:
- if it can be recycled we will find a use for it
- we pay top dollar
- starting our service is fast and easy
* All it takes is one call/email and we will handle the rest
At the bottom please put our contact information
- 800.514.2276
- maribel@salvorix27.com
- salvorix27.com

Thanks guys! I have attached our logo!

I am sorry for this late post,but could you not put anything on the back except for a return address which is 1847 Dorrance Ave Linden Vale, Ca 92874 Thank you! We have had a lot of trouble in the past with the post office when we put stuff on the back for some reason.

```html
<!DOCTYPE html>
<html lang="en">
<head>
<meta charset="utf-8">
<title>Cobalt Reclaim Partners – Postcard Back</title>
<link rel="stylesheet" href="https://fonts.googleapis.com/css2?family=Cabin:wght@400;500&display=swap">
<style>
  :root {
    --card-base: #e1e7c9;
    --card-light: #e5ead2;
    --card-warm: #dee5c2;
    --ink: #1e2b14;
    --rule: #9ba488;
    --stamp-border: #8d927d;
  }
  html, body {
    margin: 0;
    padding: 0;
    width: 1200px;
    height: 776px;
    overflow: hidden;
  }
  .postcard-back {
    position: relative;
    width: 1200px;
    height: 776px;
    background:
      linear-gradient(172deg, rgba(255,255,255,0.08) 0%, rgba(255,255,255,0) 40%),
      linear-gradient(180deg, var(--card-light) 0%, var(--card-warm) 45%, var(--card-base) 100%);
    font-family: "Cabin", sans-serif;
    color: var(--ink);
  }
  .return-address {
    position: absolute;
    left: 0;
    top: 26px;
    width: 494px;
    text-align: center;
  }
  .return-label {
    margin: 0;
    font-size: 34px;
    font-weight: 500;
    line-height: 40px;
  }
  .return-lines {
    margin: 6px 0 0;
    font-size: 30px;
    font-weight: 400;
    line-height: 35px;
    font-style: normal;
  }
  .stamp-box {
    position: absolute;
    left: 1016px;
    top: 29px;
    width: 150px;
    height: 152px;
    border: 1px solid var(--stamp-border);
  }
  .address-rules {
    position: absolute;
    left: 546px;
    top: 0;
  }
</style>
</head>
<body>
  <main class="postcard-back">
    <section class="return-address">
      <p class="return-label">Return to:</p>
      <address class="return-lines">1847 Dorrance Ave Linden Vale,<br>Ca 92874</address>
    </section>

    <div class="stamp-box" aria-label="Stamp area"></div>

    <svg class="address-rules" width="617" height="776" viewBox="0 0 617 776" aria-hidden="true">
      <g stroke="var(--rule)" stroke-width="1">
        <line x1="0" y1="379.5" x2="616" y2="379.5"/>
        <line x1="0" y1="458.5" x2="616" y2="458.5"/>
        <line x1="0" y1="537.5" x2="616" y2="537.5"/>
        <line x1="0" y1="615.5" x2="616" y2="615.5"/>
      </g>
    </svg>
  </main>
</body>
</html>
```